New Web Design Project

See attachments on the content and concept. Very important that the flow of the tiers stand out

Target Market(s)

Food and Beverage Manufacturing

Industry/Entity Type

Food and Beverage

Coding

Coded - Design and coding required

Number of Pages Required

3 page

Colors
0054AA
0677BA
7BADD7
CADEEF
E8F1F8

```html
<!DOCTYPE html>
<html lang="en">
<head>
<meta charset="utf-8">
<title>Northvale Consulting – SQF Consulting</title>
<link href="https://fonts.googleapis.com/css2?family=Anton&family=Libre+Baskerville:wght@400;700&family=Marcellus&family=Montserrat:ital,wght@0,400;0,500;0,600;0,700;1,600&display=swap" rel="stylesheet">
<style>
:root{
  --blue-deep:#0054AA;
  --blue:#0677BA;
  --blue-soft:#7BADD7;
  --blue-pale:#CADEEF;
  --blue-mist:#E8F1F8;
  --ink:#111820;
  --ink-soft:#3a4350;
  --white:#ffffff;
  --serif:'Libre Baskerville', Georgia, serif;
  --display:'Marcellus', Georgia, serif;
  --sans:'Montserrat', Arial, sans-serif;
  --num:'Anton', Impact, sans-serif;
}
*{margin:0;padding:0;box-sizing:border-box}
html,body{width:1200px;height:3333px;overflow:hidden}
body{position:relative;font-family:var(--sans);color:var(--ink);background:var(--white)}
.abs{position:absolute}
section,footer{position:absolute;left:0;width:1200px}

/* hero */
.hero{top:0;height:465px}
.hero-photo{position:absolute;inset:0;background:linear-gradient(100deg,#143a4a 0%,#2c5a55 35%,#6d8f86 60%,#b9c8c4 80%,#d9e0dd 100%)}
.hero-shade{position:absolute;inset:0;background:linear-gradient(90deg,rgba(10,30,45,.75) 0%,rgba(10,30,45,.35) 55%,rgba(0,0,0,0) 80%)}
.brand{font-family:var(--serif);font-weight:700;color:var(--white);line-height:1}
.brand .name{font-size:22px;display:block}
.brand .tag{font-family:var(--sans);font-size:6.5px;letter-spacing:1.2px;font-weight:600;display:block;margin-top:3px}
.nav{top:33px;left:412px;display:flex;gap:18px;font-size:10px;font-weight:600;letter-spacing:.6px;color:var(--white)}
.nav-phone{top:31px;left:789px;color:var(--white);font-size:12px;font-weight:600;display:flex;align-items:center;gap:6px}
.btn-solid{background:var(--blue-soft);color:var(--white);font-size:9.5px;font-weight:600;letter-spacing:.5px;display:flex;align-items:center;justify-content:center}
.hero-cta{top:27px;left:913px;width:168px;height:23px}
.hero-frame{top:0;left:250px;width:403px;height:341px;border-right:2px solid rgba(255,255,255,.85);border-bottom:2px solid rgba(255,255,255,.85)}
.hero-title{top:168px;left:118px;font-family:var(--serif);font-weight:700;color:var(--white);font-size:50px;line-height:1}
.hero-sub{top:218px;left:118px;font-family:var(--serif);font-weight:700;color:var(--white);font-size:25px}
.hero-text{top:259px;left:118px;width:470px;color:var(--white);font-size:12.5px;line-height:16px}
.btn-line{border:1.5px solid currentColor;font-size:10px;font-weight:600;letter-spacing:.6px;display:flex;align-items:center;justify-content:center}
.hero-btn{top:323px;left:118px;width:172px;height:26px;color:var(--white)}

/* services */
.services{top:465px;height:494px;background:#e3edf7}
.eyebrow{font-family:var(--serif);color:var(--blue-deep);font-size:14px;letter-spacing:.3px}
.services .eyebrow{top:28px;left:118px}
.services h2{position:absolute;top:52px;left:118px;font-weight:500;font-size:28.5px;line-height:34px;letter-spacing:.3px}
.card{top:153px;width:226px;height:244px;background:var(--white);box-shadow:0 4px 14px rgba(0,40,90,.08);text-align:center}
.card svg{display:block;margin:14px auto 0}
.card h3{font-family:var(--serif);font-weight:400;font-size:15px;line-height:17px;margin-top:10px;padding:0 20px}
.card p{font-size:10px;line-height:12.3px;color:var(--ink-soft);margin-top:14px;padding:0 18px}
.view-all{top:428px;left:516px;width:171px;height:28px;color:var(--ink);border-width:1.5px;border-radius:3px;font-weight:500}

/* benefits */
.benefits{top:959px;height:767px;background:var(--white)}
.big-title{font-family:var(--display);color:var(--blue-deep);text-align:center;width:100%;line-height:1}
.benefits .big-title{top:30px;font-size:46px;line-height:42px}
.benefits .lead{top:128px;width:100%;text-align:center;font-size:14.5px;line-height:17px}
.benefit-photo{top:231px;left:0;width:830px;height:536px;background:linear-gradient(130deg,#dfe6ec 0%,#c7d3de 40%,#9fb3c3 70%,#4f7a3a 100%)}
.benefit-panel{top:196px;left:600px;width:540px;height:485px;background:var(--white);box-shadow:0 6px 30px rgba(0,40,90,.08)}
.perk{left:40px;width:425px;height:87px;background:#f6f7f8;display:flex;align-items:flex-start;gap:14px;padding:14px 10px}
.perk svg{flex:none;margin-top:6px}
.perk h4{font-family:var(--serif);font-weight:400;font-size:13.5px;margin-bottom:5px}
.perk p{font-size:10px;line-height:12px;color:var(--ink-soft)}
.benefit-btn{top:427px;left:40px;width:169px;height:23px}

/* process */
.process{top:1726px;height:480px;background:#e6eff8}
.process .big-title{top:50px;font-size:44px}
.process .lead{top:105px;width:100%;text-align:center;font-size:14px}
.step{top:178px;width:200px;text-align:center}
.step svg{display:block;margin:0 auto}
.step h3{font-family:var(--serif);font-weight:400;font-size:16px;margin-top:20px}
.step p{font-size:10px;line-height:12.2px;color:var(--ink-soft);margin-top:28px;padding:0 6px}
.step-num{top:374px;font-family:var(--num);font-size:50px;line-height:1;color:var(--ink);width:80px;text-align:center}
.dash{top:387px}

/* testimonials */
.testimonials{top:2206px;height:432px;background:linear-gradient(180deg,#0a4b9b,#0c4690)}
.testimonials h2{position:absolute;top:40px;width:100%;text-align:center;font-family:var(--display);font-weight:400;font-size:66px;color:var(--white)}
.testimonials .lead{top:120px;width:100%;text-align:center;color:var(--white);font-size:14px}
.quote-card{top:171px;left:165px;width:885px;height:204px;background:#f7f7f7}
.quote-card blockquote{position:absolute;top:52px;left:78px;width:760px;font-size:19px;line-height:23px;color:var(--ink)}
.quote-card cite{position:absolute;top:150px;left:0;width:100%;padding-left:100px;text-align:center;font-style:italic;font-weight:600;font-size:13px}

/* consult */
.consult{top:2638px;height:446px}
.consult-photo{position:absolute;inset:0;background:linear-gradient(90deg,#3d5e52 0%,#6d7c5f 30%,#8a8a70 55%,#5f6c5a 80%,#2f4a3e 100%)}
.form-panel{top:55px;left:156px;width:347px;height:326px;background:rgba(12,70,150,.88);padding:18px 18px}
.form-panel .eyebrow{font-family:var(--sans);font-weight:700;color:var(--white);font-size:13px;letter-spacing:.4px}
.form-panel h2{color:var(--white);font-weight:700;font-size:23px;line-height:23px;margin-top:12px;letter-spacing:.3px}
.field{position:absolute;height:28px;background:var(--white);border:1px solid var(--blue-pale);font-size:11px;color:var(--ink);padding:8px 10px;font-weight:500}
.field b{color:#d33;font-weight:500}
.submit{position:absolute;top:282px;left:17px;width:312px;height:28px;background:var(--blue-soft);color:var(--white);font-weight:700;font-size:13px;letter-spacing:.6px;display:flex;align-items:center;justify-content:center}

/* footer */
.site-footer{top:3084px;height:249px;background:linear-gradient(180deg,#1d5db0 0%,#0b4aa0 40%,#0054AA 100%);color:var(--white)}
.foot-brand{top:90px;left:176px}
.foot-brand .name{font-size:22px}
.social{top:120px;width:24px;height:24px;border-radius:50%;background:var(--white)}
.foot-col h5{font-size:10.5px;font-weight:700;letter-spacing:.6px;margin-bottom:22px}
.foot-col ul{list-style:none;font-size:11px;line-height:18px}
.contact-row{left:830px;display:flex;align-items:center;gap:14px;font-size:12.5px}
.contact-row .dot{width:26px;height:26px;border-radius:50%;background:var(--white);display:flex;align-items:center;justify-content:center}
.copyright{top:196px;width:100%;text-align:center;font-size:10.5px;padding-left:40px}
</style>
</head>
<body>

<section class="hero">
  <div class="hero-photo" role="img" aria-label="Scientist in a laboratory examining a strawberry with tweezers, plants and a microscope in view"></div>
  <div class="hero-shade"></div>
  <div class="abs hero-frame"></div>
  <div class="abs brand" style="top:26px;left:116px"><span class="name">Northvale Consulting</span><span class="tag">FOOD SAFETY &amp; SQF CERTIFICATION</span></div>
  <nav class="abs nav"><span>SERVICES</span><span>BENEFITS</span><span>PROCESS</span><span>CONTACT US</span></nav>
  <div class="abs nav-phone">
    <svg width="11" height="11" viewBox="0 0 24 24"><path d="M6 2l4 4-2 3c1.5 3 4 5.5 7 7l3-2 4 4-3 4C10 21 3 14 2 5z" fill="#fff"/></svg>
    555 010 2040
  </div>
  <div class="abs btn-solid hero-cta">GET SQF CONSULTATION</div>
  <h1 class="abs hero-title">SQF Consulting</h1>
  <div class="abs hero-sub">Implementation &amp; On Boarding</div>
  <p class="abs hero-text">We help food and beverage manufacturers achieve and maintain SQF certification with confidence, using practical programs and digital tools that work on the floor - not just on audit day.</p>
  <div class="abs btn-line hero-btn">GET SQF CONSULTATION</div>
</section>

<section class="services">
  <div class="abs eyebrow">SERVICES WE OFFER</div>
  <h2>Seamless SQF implementation and onboarding for<br>certified food safety excellence</h2>

  <div class="abs card" style="left:114px">
    <svg width="84" height="56" viewBox="0 0 84 56" fill="none" stroke="#0054AA" stroke-width="2"><rect x="4" y="14" width="46" height="30" rx="2"/><path d="M20 50h22M30 44v6M20 24l-5 5 5 5M34 24l5 5-5 5M29 22l-4 14"/><circle cx="64" cy="18" r="9"/><circle cx="64" cy="18" r="3.5"/><path d="M64 5v4M64 27v4M51 18h4M73 18h4M55 9l3 3M70 24l3 3M73 9l-3 3M58 24l-3 3"/></svg>
    <h3>SQF Program<br>Design</h3>
    <p>We design your complete SQF system from scratch HACCP/food safety plans, prereq-uisite programs, SOPs, forms, logs, and all required documen-tation tailored to your facility.</p>
  </div>
  <div class="abs card" style="left:359px">
    <svg width="84" height="56" viewBox="0 0 84 56" fill="none" stroke="#0054AA" stroke-width="2"><rect x="12" y="4" width="60" height="38" rx="2"/><rect x="17" y="9" width="50" height="28"/><path d="M34 50h16M42 42v8"/><circle cx="42" cy="23" r="7"/><circle cx="42" cy="23" r="2.5"/><path d="M42 13v3M42 30v3M32 23h3M49 23h3"/></svg>
    <h3>Digital Platform<br>Build</h3>
    <p>We build your SQF program directly into modern food safety software like PrepTrack or SafeLedger - digitizing forms, checklists, monitoring logs, and workflows so your team runs paperless.</p>
  </div>
  <div class="abs card" style="left:608px">
    <svg width="90" height="60" viewBox="0 0 90 60" fill="none" stroke="#0054AA" stroke-width="2"><path d="M14 56h20V44h16V32h16V20h14"/><circle cx="28" cy="18" r="4"/><path d="M28 22v14l-6 12M28 36l6 12M22 28h12"/><circle cx="50" cy="10" r="4"/><path d="M50 14v12l-5 10M50 26l5 8M38 20l12 0"/><path d="M66 14l14-10M72 4h8v8"/></svg>
    <h3>Coaching &amp;<br>Support</h3>
    <p>After building your system, we coach your team to own and maintain it day-to-day. You run the program; we provide ongoing expert guidance so you stay audit-ready at all times.</p>
  </div>
  <div class="abs card" style="left:853px">
    <svg width="84" height="56" viewBox="0 0 84 56" fill="none" stroke="#0054AA" stroke-width="2"><rect x="18" y="4" width="40" height="48" rx="2"/><path d="M24 24l8-6 8 5 12-9M24 34h22M24 40h18M24 46h14"/><circle cx="56" cy="40" r="8"/><path d="M52 40l3 3 5-6M62 46l8 8"/></svg>
    <h3>Gap Assessments</h3>
    <p style="margin-top:31px">We evaluate where your facility stands against SQF require-ments, identify gaps, and provide a clear roadmap to close them before your audit - no surprises on certification day.</p>
  </div>

  <div class="abs btn-line view-all">VIEW ALL SERVICES</div>
</section>

<section class="benefits" id="benefits">
  <h2 class="abs big-title">Built for Small &amp;<br>Mid- Size Manufacturers</h2>
  <p class="abs lead">You don't need to hire a full-time food safety director or figure out SQF alone.<br>We bring the expertise and technology - you stay focused on production.</p>

  <div class="abs benefit-photo" role="img" aria-label="Gloved hand holding tweezers over a leafy green sample on a clipboard"></div>

  <div class="abs benefit-panel">
    <div class="abs perk" style="top:19px">
      <svg width="46" height="34" viewBox="0 0 46 34" fill="none" stroke="#0054AA" stroke-width="2"><circle cx="18" cy="17" r="13"/><path d="M22 11h-6a3 3 0 000 6h4a3 3 0 010 6h-6M18 8v3M18 23v3M34 10h10M34 17h10M34 24h10"/></svg>
      <div><h4>Lower Cost Than a Full-Time Hire</h4><p>Get a complete SQF team-program design, digital imple-mentation, and coaching - at a fraction of the cost of hiring a full-time SQF Practitioner.</p></div>
    </div>
    <div class="abs perk" style="top:117px">
      <svg width="50" height="40" viewBox="0 0 50 40" fill="none" stroke="#0054AA" stroke-width="2"><rect x="2" y="2" width="40" height="28" rx="3"/><path d="M2 10h40M10 17l-4 4 4 4M18 17l4 4-4 4"/><circle cx="38" cy="30" r="6"/><circle cx="38" cy="30" r="2"/><path d="M38 21v3M38 36v3M29 30h3M44 30h3"/></svg>
      <div><h4>Your Program Lives in Software</h4><p>No more binders and spreadsheets. Your SQF system is built into PrepTrack or SafeLedger - organized, accessible, and always audit-ready.</p></div>
    </div>
    <div class="abs perk" style="top:216px">
      <svg width="46" height="42" viewBox="0 0 46 42" fill="none" stroke="#0054AA" stroke-width="2"><circle cx="23" cy="14" r="8"/><path d="M13 16v-4a10 10 0 0120 0v4M33 16v3l-6 2M7 40c0-9 7-14 16-14s16 5 16 14z"/></svg>
      <div><h4>You Own It, We Support It</h4><p>We build the system and train your team. You maintain and run it day-to-day. We stay on call with coaching and advisory so you never feel stuck.</p></div>
    </div>
    <div class="abs perk" style="top:316px">
      <svg width="48" height="44" viewBox="0 0 48 44" fill="none" stroke="#0054AA" stroke-width="2"><circle cx="20" cy="22" r="12"/><circle cx="20" cy="22" r="4"/><path d="M20 6v4M20 34v4M4 22h4M32 22h4M9 11l3 3M28 30l3 3M31 11l-3 3M12 30l-3 3M36 24l8 8M40 40l4-8"/></svg>
      <div><h4>Flexible, Low-Risk Engagement</h4><p>Start with a 3-month commitment, then go month-to-month. Cancel anytime with 30 days notice. We earn your business every month.</p></div>
    </div>
    <div class="abs btn-solid benefit-btn">GET SQF CONSULTATION</div>
  </div>
</section>

<section class="process" id="process">
  <h2 class="abs big-title">From Discovery to Certification</h2>
  <p class="abs lead">A clear, structured path that takes the guesswork out of SQF</p>

  <div class="abs step" style="left:130px">
    <svg width="64" height="56" viewBox="0 0 64 56" fill="none" stroke="#0677BA" stroke-width="2"><path d="M14 8l8 8-5 5c3 6 8 11 14 14l5-5 8 8-6 7C20 44 8 32 6 15z"/><path d="M36 10a12 12 0 0112 12M36 3a19 19 0 0119 19"/></svg>
    <h3>Discovery Call</h3>
    <p>We learn about your facility, your current systems, and where you are in the SQF journey. No pres-sure - just a conversation.</p>
  </div>
  <div class="abs step" style="left:395px">
    <svg width="64" height="56" viewBox="0 0 64 56" fill="none" stroke="#0677BA" stroke-width="2"><rect x="12" y="2" width="36" height="46" rx="2"/><path d="M18 10h24M18 16h18"/><circle cx="30" cy="30" r="9"/><path d="M26 30l3 3 5-6M37 37l10 10"/></svg>
    <h3>Gap Assessment</h3>
    <p>We evaluate your facility against SQF requirements, identify what's missing, and give you a clear roadmap with priorities.</p>
  </div>
  <div class="abs step" style="left:624px">
    <svg width="64" height="56" viewBox="0 0 64 56" fill="none" stroke="#0677BA" stroke-width="2"><circle cx="32" cy="28" r="22"/><circle cx="32" cy="28" r="11"/><circle cx="32" cy="28" r="4"/><path d="M32 14v3M32 39v3M18 28h3M43 28h3M52 18l2-6 4 5"/></svg>
    <h3>Build &amp; Implement</h3>
    <p>We design your SQF program and build it directly into your digital food safety platform-forms, logs, SOPs, HACCP plans, all of it.</p>
  </div>
  <div class="abs step" style="left:870px">
    <svg width="70" height="56" viewBox="0 0 70 56" fill="none" stroke="#0677BA" stroke-width="2"><circle cx="22" cy="18" r="5"/><circle cx="46" cy="18" r="5"/><path d="M12 34c0-6 4-9 10-9s10 3 10 9M36 34c0-6 4-9 10-9s10 3 10 9"/><circle cx="14" cy="40" r="4"/><circle cx="34" cy="40" r="4"/><circle cx="54" cy="40" r="4"/><path d="M6 54c0-5 3-7 8-7s8 2 8 7M26 54c0-5 3-7 8-7s8 2 8 7M46 54c0-5 3-7 8-7s8 2 8 7"/><rect x="48" y="2" width="18" height="10" rx="2"/></svg>
    <h3>Coach &amp; Certify</h3>
    <p>We train your team, run mock audits, and prepare you for certi-fication day. Then we stay on as your ongoing SQF advisory part-ner.</p>
  </div>

  <div class="abs step-num" style="left:160px">01</div>
  <div class="abs step-num" style="left:423px">02</div>
  <div class="abs step-num" style="left:684px">03</div>
  <div class="abs step-num" style="left:937px">04</div>
  <svg class="abs dash" style="left:246px" width="164" height="22" viewBox="0 0 164 22" fill="none" stroke="#222" stroke-width="1.2"><path d="M2 14C40 -2 90 30 156 12" stroke-dasharray="5 4"/><path d="M150 8l7 4-6 5" fill="#222"/></svg>
  <svg class="abs dash" style="left:508px" width="164" height="22" viewBox="0 0 164 22" fill="none" stroke="#222" stroke-width="1.2"><path d="M2 14C40 -2 90 30 156 12" stroke-dasharray="5 4"/><path d="M150 8l7 4-6 5" fill="#222"/></svg>
  <svg class="abs dash" style="left:768px" width="164" height="22" viewBox="0 0 164 22" fill="none" stroke="#222" stroke-width="1.2"><path d="M2 14C40 -2 90 30 156 12" stroke-dasharray="5 4"/><path d="M150 8l7 4-6 5" fill="#222"/></svg>
</section>

<section class="testimonials">
  <h2>Testimonials</h2>
  <p class="abs lead">Real client experiences that showcase trust, quality, and proven results</p>
  <div class="abs quote-card">
    <blockquote>"Northvale Consulting Group didn't just hand us a binder. They built our entire SQF system into software and coached our team until we owned it. We passed our first audit with confidence."</blockquote>
    <cite>SQF-Certified Manufacturing Client</cite>
  </div>
</section>

<section class="consult" id="contact">
  <div class="consult-photo" role="img" aria-label="Food safety specialist in a lab coat working on a laptop in a greenhouse laboratory"></div>
  <form class="abs form-panel">
    <div class="eyebrow">GET SQF CONSULTATION</div>
    <h2>Start Your SQF<br>Compliance Journey</h2>
    <div class="field" style="top:103px;left:17px;width:152px">First Name <b>*</b></div>
    <div class="field" style="top:103px;left:178px;width:151px">Last Name <b>*</b></div>
    <div class="field" style="top:139px;left:17px;width:152px">Phone Number<b>*</b></div>
    <div class="field" style="top:139px;left:178px;width:151px">Email Address</div>
    <div class="field" style="top:176px;left:17px;width:312px;display:flex;justify-content:space-between">Services Looking for
      <svg width="12" height="10" viewBox="0 0 12 10"><path d="M1 3l5 5 5-5" fill="none" stroke="#111" stroke-width="1.5"/></svg></div>
    <div class="field" style="top:215px;left:17px;width:312px;height:60px">Address<b>*</b></div>
    <div class="submit">SUBMIT</div>
  </form>
</section>

<footer class="site-footer">
  <div class="abs brand foot-brand"><span class="name">Northvale Consulting</span><span class="tag">FOOD SAFETY &amp; SQF CERTIFICATION</span></div>
  <div class="abs social" style="left:231px"></div>
  <div class="abs social" style="left:266px"></div>

  <div class="abs foot-col" style="top:26px;left:450px">
    <h5>NAVIGATION</h5>
    <ul><li>Services</li><li>Benefits</li><li>Process</li><li>Contact us</li><li>Get SQF Consultation</li></ul>
  </div>
  <div class="abs foot-col" style="top:26px;left:617px">
    <h5>SERVICES WE &nbsp;OFFER</h5>
    <ul style="margin-top:-4px"><li>SQF Program Design</li><li>Digital Platform Build</li><li>Coaching &amp; Support</li><li>Gap Assessments</li></ul>
  </div>
  <div class="abs foot-col" style="top:26px;left:870px"><h5>CONTACT US</h5></div>

  <div class="abs contact-row" style="top:50px">
    <span class="dot"><svg width="13" height="13" viewBox="0 0 24 24"><path d="M6 2l4 4-2 3c1.5 3 4 5.5 7 7l3-2 4 4-3 4C10 21 3 14 2 5z" fill="#0054AA"/></svg></span>
    <span style="font-weight:600;font-size:14px">555-010-7788</span>
  </div>
  <div class="abs contact-row" style="top:80px">
    <span class="dot"><svg width="14" height="11" viewBox="0 0 14 11" fill="none" stroke="#0054AA" stroke-width="1.5"><rect x="1" y="1" width="12" height="9"/><path d="M1 1l6 5 6-5"/></svg></span>
    <span style="text-decoration:underline">info@northvaleconsulting.example</span>
  </div>
  <div class="abs contact-row" style="top:110px">
    <span class="dot"><svg width="11" height="14" viewBox="0 0 11 14"><path d="M5.5 0a5.5 5.5 0 00-5.5 5.5C0 9.5 5.5 14 5.5 14S11 9.5 11 5.5A5.5 5.5 0 005.5 0zm0 7.5a2 2 0 110-4 2 2 0 010 4z" fill="#0054AA"/></svg></span>
    <span>Northvale Consulting Group</span>
  </div>

  <p class="abs copyright">© 2026 Northvale Consulting Group . All Rights Reserved.</p>
</footer>

</body>
</html>
```